MRHT Needs Fundraiser Dinner Invite!!

The Marisol Hendrick Trust, a 501 3(c) non for profit has a yearly fundraiser, with varying themes. Last year it was "cowboys" and "cowgirls"
This year, it is Club Orchid, or 70's disco music. I have uploaded last years invite for reference, some stock photography for inspiration. You are not limited to using the stock photos.

Annual MRHT Fundraiser Dinner
October 13th, 2022
Starts: 6:30pm
RSVP By: September 20th
Place: The Bramwell
Price: $135 per ticket

Target Market(s)

Donors, Business People, Every person

Industry/Entity Type

Non for Profit

Font styles to use
Sans Serif

Colors
0054AA
0677BA
7BADD7
CADEEF
E8F1F8
E54698
E96AAD
F1A4CE
F9D9EA
FCEFF6
6B429C
8869AF
B7A5CE
E3DAEB
F3F0F8

Requirements
Must have
• The invite should be 5x7, be sophisticated as the clientele are mainly business people that come to support the cause. It should be fun and inviting at the same time.

```html
<!DOCTYPE html>
<html lang="en">
<head>
<meta charset="utf-8">
<title>MRHT Annual Fundraiser Dinner Invite</title>
<link rel="stylesheet" href="https://fonts.googleapis.com/css2?family=Montserrat:wght@600;700;800;900&display=swap">
<style>
  :root {
    --page: #ffffff;
    --blush: #f2dfe9;
    --pink: #e54698;
    --pink-mid: #e96aad;
    --pink-soft: #f1a4ce;
    --magenta: #d42fa6;
    --violet: #6b429c;
    --violet-mid: #8869af;
    --lilac: #b7a5ce;
    --pearl: #f3f0f3;
    --pearl-shade: #d9d6da;
    --teal-band: rgba(176, 232, 228, 0.72);
    --magenta-band: rgba(222, 52, 170, 0.80);
    --white: #ffffff;
  }
  * { margin: 0; padding: 0; box-sizing: border-box; }
  html, body {
    width: 1200px; height: 1000px; overflow: hidden;
    background: var(--page);
    font-family: "Montserrat", Arial, sans-serif;
  }
  .invite {
    position: absolute; left: 237px; top: 241px;
    width: 754px; height: 531px;
    background: var(--blush);
    overflow: hidden;
  }
  .scenery { position: absolute; inset: 0; width: 754px; height: 531px; }
  .copy { position: absolute; text-align: center; transform: translateX(-50%); white-space: nowrap; }
  .trust-name {
    left: 306px; top: 120px;
    font-size: 17px; font-weight: 700; color: var(--violet-mid);
    letter-spacing: 0.3px;
  }
  .kicker {
    left: 313px; top: 168px;
    font-size: 29px; font-weight: 800; color: var(--pink); letter-spacing: 0.5px;
  }
  .acronym {
    left: 312px; top: 198px;
    font-size: 82px; font-weight: 900; line-height: 1;
    color: var(--violet-mid); letter-spacing: 2px;
  }
  .event-title {
    left: 315px; top: 268px;
    font-size: 29px; font-weight: 800; color: var(--pink); letter-spacing: 0.3px;
  }
  .band-text {
    top: 374px; font-size: 16px; font-weight: 700; line-height: 19px; letter-spacing: 0.2px;
  }
  .band-text.when { left: 158px; color: var(--white); }
  .band-text.where { left: 475px; color: var(--pink); }
  .price { left: 650px; top: 221px; color: var(--magenta); font-weight: 800; }
  .price .amount { display: block; font-size: 36px; line-height: 38px; letter-spacing: -0.5px; }
  .price .unit { display: block; font-size: 12px; font-weight: 700; letter-spacing: 0.6px; color: var(--violet-mid); }
</style>
</head>
<body>
<main class="invite">
  <svg class="scenery" viewBox="0 0 754 531" aria-hidden="false">
    <defs>
      <radialGradient id="pearl" cx="0.38" cy="0.32" r="0.75">
        <stop offset="0" stop-color="#ffffff"/>
        <stop offset="0.6" stop-color="var(--pearl)"/>
        <stop offset="1" stop-color="var(--pearl-shade)"/>
      </radialGradient>
      <radialGradient id="gloss" cx="0.35" cy="0.3" r="0.8">
        <stop offset="0" stop-color="#ffe3f1"/>
        <stop offset="0.35" stop-color="var(--pink-mid)"/>
        <stop offset="0.8" stop-color="var(--magenta)"/>
        <stop offset="1" stop-color="#9a5fd0"/>
      </radialGradient>
      <radialGradient id="mirror" cx="0.4" cy="0.35" r="0.8">
        <stop offset="0" stop-color="#c9f0ff"/>
        <stop offset="0.4" stop-color="#d77fe6"/>
        <stop offset="1" stop-color="#9a2f9c"/>
      </radialGradient>
    </defs>

    <circle class="sphere pearl" cx="92" cy="102" r="105" fill="url(#pearl)"/>
    <circle class="sphere gloss" cx="83" cy="98" r="41" fill="url(#gloss)"/>
    <circle class="sphere gloss" cx="465" cy="96" r="106" fill="url(#gloss)"/>
    <circle class="sphere pearl" cx="565" cy="8" r="100" fill="url(#pearl)"/>
    <circle class="disco-ball" cx="655" cy="114" r="97" fill="url(#mirror)" role="img" aria-label="Mirrored disco ball"/>
    <circle class="sphere pearl" cx="304" cy="272" r="222" fill="url(#pearl)"/>
    <circle class="sphere pearl price-disc" cx="650" cy="247" r="55" fill="url(#pearl)"/>
    <circle class="disco-ball" cx="51" cy="376" r="131" fill="url(#mirror)" role="img" aria-label="Mirrored disco ball"/>
    <circle class="disco-ball" cx="531" cy="548" r="131" fill="url(#mirror)" role="img" aria-label="Mirrored disco ball"/>
    <circle class="sphere gloss" cx="717" cy="462" r="146" fill="url(#gloss)"/>

    <rect class="info-band when-band" x="0" y="339" width="307" height="113" fill="var(--magenta-band)"/>
    <rect class="info-band where-band" x="307" y="339" width="447" height="113" fill="var(--teal-band)"/>

    <circle class="sphere gloss" cx="197" cy="436" r="64" fill="url(#gloss)"/>
    <circle class="sphere gloss" cx="735" cy="436" r="46" fill="url(#gloss)"/>
  </svg>

  <p class="copy trust-name">The Marisol Hendrick Trust</p>
  <p class="copy kicker">ANNUAL</p>
  <h1 class="copy acronym">MRHT</h1>
  <h2 class="copy event-title">FUNDRAISER DINNER</h2>

  <p class="copy band-text when">OCTOBER 13TH, 2022<br>STARTS&nbsp; 6:30PM</p>
  <p class="copy band-text where">PLACE: THE BRAMWELL<br>RSVP BY: SEPTEMBER 20TH</p>

  <p class="copy price"><span class="amount">$135</span><span class="unit">PER TICKET</span></p>
</main>
</body>
</html>
```